Very visible CoWorking Building Sign overlooking downtown LA and 110 freeway

Our building is drab but very visible and in the best location. We need a great sign for our monolith that overlooks downtown LA and the 100 freeway. We are a new CoWorking business and would like to have a few things we do on the sign: private offices, virtual offices, CoWorking Lounge. Everything we have seen is ho-hum. Can you get us noticed? We need people to know what we do and that we are here but in a creative, professional, unique sign.
Target Market(s)
People who have a business in DTLA, remote workers and those who work from home who need a professional address.
Requirements
Must have
- Our logo (which can be somewhat reimagined) which has our address 2770 on it. The three things we focus on: Private Offices, Virtual Offices, CoWorking Lounge. Incorporate some Navy. Readable from several hundred feet away.
Nice to have
- Mural feel? Something inspirational in this crazy COVID times? Graphics? Color block. I like the idea of decorative but it has to be readable as a building sign. The same with the use of colors. Our colors are grays and navy but with a pop of the chartreuse (we have 2 velvet chartreuse chairs in the space). Helpful to view our website: Brackmere2770.com.
Should not have
- Not too graffiti. Keep it professional but unique and wow.

```html
<!DOCTYPE html>
<html lang="en">
<head>
<meta charset="utf-8">
<title>Brackmere2770 Building Sign</title>
<link href="https://fonts.googleapis.com/css2?family=Libre+Baskerville:wght@700&family=Tinos:wght@700&display=swap" rel="stylesheet">
<style>
  :root {
    --navy: #0e2a4f;
    --blue: #0862ad;
    --chartreuse: #8cc63f;
    --white: #ffffff;
    --backdrop: #c4c4c4;
  }
  * { margin: 0; padding: 0; box-sizing: border-box; }
  html, body {
    width: 1200px;
    height: 1097px;
    overflow: hidden;
    background: var(--backdrop);
  }
  .sign {
    position: absolute;
    left: 288px;
    top: 28px;
    width: 624px;
    height: 1040px;
    background: var(--navy);
    overflow: hidden;
    color: var(--white);
  }
  .sign__waves {
    position: absolute;
    left: 0;
    top: 0;
    width: 624px;
    height: 1040px;
  }
  .brand {
    position: absolute;
    left: 30px;
    right: 30px;
    top: 46px;
    text-align: right;
    font-family: "Libre Baskerville", "Times New Roman", serif;
    font-weight: 700;
    color: var(--white);
    line-height: 1;
  }
  .brand__name {
    display: block;
    font-size: 60px;
    letter-spacing: -1px;
    text-align: center;
  }
  .brand__domain {
    display: block;
    font-size: 40px;
    margin-top: 2px;
    padding-right: 6px;
  }
  .brand__rule {
    position: absolute;
    left: 256px;
    top: 184px;
    width: 114px;
    height: 6px;
    background: var(--white);
  }
  .service {
    position: absolute;
    left: 26px;
    height: 110px;
    display: flex;
    align-items: center;
  }
  .service__icon {
    width: 108px;
    height: 108px;
    border-radius: 50%;
    background: var(--chartreuse);
    border: 2px solid var(--white);
    flex: none;
  }
  .service__label {
    margin-left: 26px;
    font-family: "Libre Baskerville", "Times New Roman", serif;
    font-weight: 700;
    font-size: 54px;
    line-height: 1.02;
    color: var(--white);
    text-transform: uppercase;
    letter-spacing: -0.5px;
  }
  .service--private { top: 245px; }
  .service--virtual { top: 445px; }
  .service--lounge { top: 645px; }
  .service-divider {
    position: absolute;
    left: 160px;
    width: 183px;
    height: 2px;
    background: var(--white);
  }
  .service-divider--first { top: 400px; }
  .service-divider--second { top: 603px; }
  .phone {
    position: absolute;
    left: 0;
    right: 0;
    top: 900px;
    text-align: center;
    font-family: "Tinos", "Times New Roman", serif;
    font-weight: 700;
    font-size: 100px;
    line-height: 1;
    color: var(--white);
    letter-spacing: -1px;
  }
</style>
</head>
<body>
  <main class="sign">
    <svg class="sign__waves" viewBox="0 0 624 1040" aria-hidden="true">
      <path fill="var(--chartreuse)" d="M0,775 C110,840 190,880 260,895 L0,905 Z"/>
      <path fill="var(--chartreuse)" d="M400,880 C480,860 560,850 624,850 L624,900 L400,900 Z"/>
      <path fill="var(--blue)" d="M0,800 C140,880 300,905 450,865 C530,843 590,830 624,828 L624,842 C580,845 520,860 450,882 C300,925 140,905 0,845 Z"/>
      <path fill="var(--white)" d="M0,815 C140,890 300,915 450,873 C530,850 590,840 624,838 L624,858 C580,860 520,872 450,892 C300,935 140,915 0,855 Z"/>
      <path fill="var(--blue)" d="M0,850 C140,912 300,932 450,890 C520,870 580,860 624,862 L624,1040 L0,1040 Z"/>
      <path fill="var(--chartreuse)" d="M400,892 C470,870 560,862 624,862 L624,875 C560,875 480,885 400,905 Z"/>
    </svg>

    <div class="brand">
      <span class="brand__name">Brackmere2770</span>
      <span class="brand__domain">.com</span>
    </div>
    <div class="brand__rule"></div>

    <section class="service service--private">
      <div class="service__icon" role="img" aria-label="Icon of a private office desk with chair, lamp and picture"></div>
      <h2 class="service__label">Private<br>Offices</h2>
    </section>
    <div class="service-divider service-divider--first"></div>

    <section class="service service--virtual">
      <div class="service__icon" role="img" aria-label="Icon of a reception desk with mail envelope and plant"></div>
      <h2 class="service__label">Virtual<br>Offices</h2>
    </section>
    <div class="service-divider service-divider--second"></div>

    <section class="service service--lounge">
      <div class="service__icon" role="img" aria-label="Icon of people meeting around a shared table"></div>
      <h2 class="service__label">Coworking<br>Lounge</h2>
    </section>

    <p class="phone">310.555.2770</p>
  </main>
</body>
</html>
```